BrivaTrek Freight Services Business cards

Would like a very unique design catchy but professional for business cards. Please use log provided.Marlon WellsCeo and Founder TransCon Logistix Solutions1-888-913-3225mwells@tlsolutionsus.comwww.bfservicesco.com

```html
<!DOCTYPE html>
<html lang="en">
<head>
<meta charset="utf-8">
<title>BrivaTrek Freight Services – Business Cards</title>
<link rel="stylesheet" href="https://fonts.googleapis.com/css2?family=Lato:wght@400;700;900&display=swap">
<style>
  :root{
    --stage:#e4e4e4;
    --brand-blue:#1673bd;
    --brand-red:#e8232f;
    --card-white:#ffffff;
    --panel-grey:#ececec;
    --ink:#3a3a3a;
  }
  *{margin:0;padding:0;box-sizing:border-box}
  html,body{width:1200px;height:900px;overflow:hidden}
  body{background:var(--stage);font-family:"Lato",sans-serif;position:relative}

  .card{position:absolute;width:560px;height:320px;border-radius:22px;overflow:hidden;
        box-shadow:0 6px 18px rgba(0,0,0,.12)}

  /* back side */
  .card-back{left:90px;top:70px;background:var(--brand-blue);
             display:flex;align-items:center;justify-content:center;gap:14px}
  .card-back .mark-square{width:22px;height:22px;background:var(--card-white)}
  .card-back .brand-name{color:var(--card-white);font-weight:700;font-size:28px;letter-spacing:.5px}

  /* front side */
  .card-front{left:550px;top:510px;background:var(--card-white)}
  .panel-top{position:absolute;left:46%;top:0;right:0;height:22%;background:var(--panel-grey)}
  .panel-side{position:absolute;left:74%;top:0;right:0;height:76%;background:var(--panel-grey)}
  .panel-strip{position:absolute;left:76%;top:0;width:7%;height:76%;background:#f6f6f6}

  .brand-lockup{position:absolute;left:34px;top:92px;display:flex;align-items:center;gap:10px}
  .brand-lockup .mark-square{width:16px;height:16px;background:var(--brand-blue)}
  .brand-lockup .brand-name{color:var(--brand-blue);font-weight:700;font-size:21px;letter-spacing:.4px}
  .brand-rule{position:absolute;left:34px;top:128px;width:270px;height:2px;background:var(--brand-red)}

  .person{position:absolute;left:34px;top:160px}
  .person-name{font-weight:900;font-size:22px;letter-spacing:.5px;text-transform:uppercase;color:var(--brand-blue)}
  .person-name .last{color:var(--brand-red)}
  .person-title{font-size:14px;color:var(--ink);margin-top:2px}

  .contact{position:absolute;left:34px;top:236px;list-style:none;font-size:14px;color:var(--ink)}
  .contact li{display:flex;align-items:center;gap:8px;margin-bottom:5px}
  .contact svg{width:12px;height:12px;fill:var(--brand-blue)}

  .website{position:absolute;right:26px;top:176px;font-size:13px;color:var(--brand-blue)}
</style>
</head>
<body>

<section class="card card-back" aria-label="Card back">
  <span class="mark-square"></span>
  <span class="brand-name">BrivaTrek Freight Services</span>
</section>

<section class="card card-front" aria-label="Card front">
  <div class="panel-top"></div>
  <div class="panel-side"></div>
  <div class="panel-strip"></div>

  <div class="brand-lockup">
    <span class="mark-square"></span>
    <span class="brand-name">BrivaTrek Freight Services</span>
  </div>
  <div class="brand-rule"></div>

  <div class="person">
    <p class="person-name">Dustin <span class="last">Harrow</span></p>
    <p class="person-title">CEO and Founder</p>
  </div>

  <ul class="contact">
    <li>
      <svg viewBox="0 0 24 24" aria-hidden="true"><path d="M6.6 10.8a15.1 15.1 0 0 0 6.6 6.6l2.2-2.2a1 1 0 0 1 1-.25 11.4 11.4 0 0 0 3.6.57 1 1 0 0 1 1 1V20a1 1 0 0 1-1 1A17 17 0 0 1 3 4a1 1 0 0 1 1-1h3.5a1 1 0 0 1 1 1c0 1.25.2 2.45.57 3.57a1 1 0 0 1-.25 1z"/></svg>
      1-888-472-6081
    </li>
    <li>
      <svg viewBox="0 0 24 24" aria-hidden="true"><path d="M2 5h20v14H2z M2 5l10 8 10-8" /></svg>
      dharrow@bfservicesco.com
    </li>
  </ul>

  <p class="website">www.bfservicesco.com</p>
</section>

</body>
</html>
```